Insurance Pull Down Bar Ad

I need a simple magazine ad. At the top of the ad will read "Need Insurance? We Can Help." Below it will be a pull down bar that has been clicked on by a cursor. In the pull-down bar will be (one above the other) "medical, dental, life, disability, office-overhead, personal accident, travel, medical evacuation, critical illness and hospital indemnity."

In the attached file there is a logo in the upper left corner. It has our name and exclusively endorsed below it. Use this in the ad.

Colors should go with the logo attached.

We will need social media icons at the bottom: Facebook, Youtube, Twitter, LinkedIn

I need it in a file that a graphic artist can edit.

Insurance

```html
<!DOCTYPE html>
<html lang="en">
<head>
<meta charset="utf-8">
<title>Need Insurance? We Can Help.</title>
<link rel="stylesheet" href="https://fonts.googleapis.com/css2?family=Arimo:wght@700&family=Questrial&family=Lora:ital@1&display=swap">
<style>
  :root {
    --backdrop: #6b6b6b;
    --crimson: #b5173a;
    --crimson-dark: #8e0f2b;
    --page-top: #e4eded;
    --page-bottom: #bfd2d3;
    --panel-top: #ffffff;
    --panel-bottom: #e3e3e3;
    --rule: #d2d2d2;
    --ink: #222222;
    --ink-soft: #555555;
    --social-navy: #3b5998;
    --social-red: #cc2020;
    --social-sky: #2aa3ef;
    --social-blue: #1d6fb0;
  }
  * { margin: 0; padding: 0; box-sizing: border-box; }
  html, body { width: 1200px; height: 1000px; overflow: hidden; }
  body { background: var(--backdrop); position: relative; font-family: "Questrial", sans-serif; }

  .ad-page {
    position: absolute; left: 290px; top: 70px; width: 620px; height: 860px;
    background: var(--crimson); padding: 22px;
  }
  .ad-inner {
    position: relative; width: 100%; height: 100%;
    background: radial-gradient(ellipse at 50% 35%, var(--page-top), var(--page-bottom));
  }

  .dropdown-header {
    position: absolute; left: 48px; top: 52px; width: 480px; height: 52px;
    background: linear-gradient(var(--panel-top), var(--panel-bottom));
    border-radius: 26px 6px 6px 26px;
    box-shadow: 0 3px 6px rgba(0,0,0,.25);
    display: flex; align-items: center; padding-left: 30px;
    font-family: "Arimo", sans-serif; font-weight: 700; font-size: 23px; color: var(--ink);
  }
  .dropdown-toggle {
    position: absolute; right: 0; top: 0; width: 58px; height: 52px;
    background: linear-gradient(#d22a4e, var(--crimson-dark));
    border-radius: 0 6px 6px 0;
    display: flex; align-items: center; justify-content: center;
  }

  .dropdown-list {
    position: absolute; left: 70px; top: 120px; width: 440px; height: 460px;
    background: linear-gradient(var(--panel-top), var(--panel-bottom));
    border-radius: 34px;
    box-shadow: 0 4px 10px rgba(0,0,0,.25);
    list-style: none; padding-top: 12px;
  }
  .dropdown-item {
    position: relative; height: 44px; display: flex; align-items: center;
    padding-left: 26px; gap: 18px;
    border-bottom: 1px solid var(--rule);
    font-size: 25px; color: var(--ink);
  }
  .dropdown-item:last-child { border-bottom: none; }
  .item-arrow {
    width: 24px; height: 24px; background: var(--crimson);
    border-radius: 3px; flex: none;
    display: flex; align-items: center; justify-content: center;
  }
  .dropdown-item.is-selected {
    margin: 0 -40px; padding-left: 66px; height: 46px;
    background: linear-gradient(#d0264b, var(--crimson-dark));
    color: #fff; font-family: "Arimo", sans-serif; font-weight: 700;
    border-radius: 4px; border-bottom: none;
    box-shadow: 0 3px 6px rgba(0,0,0,.3);
  }
  .dropdown-item.is-selected .item-arrow { background: #fff; }
  .cursor { position: absolute; right: 60px; top: 10px; }

  .social-links { position: absolute; right: 30px; top: 600px; display: flex; gap: 8px; }
  .social-icon { width: 32px; height: 32px; border-radius: 5px; }
  .social-icon.network-one { background: var(--social-navy); }
  .social-icon.network-two { background: var(--social-red); }
  .social-icon.network-three { background: var(--social-sky); }
  .social-icon.network-four { background: var(--social-blue); }

  .brand { position: absolute; left: 40px; top: 690px; }
  .brand-row { display: flex; align-items: center; gap: 12px; }
  .brand-mark { width: 44px; height: 44px; background: var(--crimson); flex: none; }
  .brand-name { font-size: 24px; color: var(--crimson); line-height: 1.1; }
  .brand-name span { display: block; white-space: nowrap; }
  .brand-endorsement {
    margin-top: 14px; font-family: "Lora", serif; font-style: italic;
    font-size: 15px; color: var(--ink-soft);
  }
</style>
</head>
<body>
  <div class="ad-page">
    <div class="ad-inner">
      <div class="dropdown-header">“Need Insurance? We Can Help.”
        <span class="dropdown-toggle">
          <svg width="20" height="14" viewBox="0 0 20 14"><path d="M2 3 L10 11 L18 3" fill="none" stroke="#fff" stroke-width="4"/></svg>
        </span>
      </div>

      <ul class="dropdown-list">
        <li class="dropdown-item"><span class="item-arrow"><svg width="10" height="12" viewBox="0 0 10 12"><path d="M2 1 L8 6 L2 11" fill="none" stroke="#fff" stroke-width="2.5"/></svg></span>Medical</li>
        <li class="dropdown-item"><span class="item-arrow"><svg width="10" height="12" viewBox="0 0 10 12"><path d="M2 1 L8 6 L2 11" fill="none" stroke="#fff" stroke-width="2.5"/></svg></span>Dental</li>
        <li class="dropdown-item is-selected"><span class="item-arrow"><svg width="10" height="12" viewBox="0 0 10 12"><path d="M2 1 L8 6 L2 11" fill="none" stroke="#b5173a" stroke-width="2.5"/></svg></span>Life
          <svg class="cursor" width="26" height="34" viewBox="0 0 26 34"><path d="M2 2 L2 28 L9 22 L14 32 L19 30 L14 20 L23 20 Z" fill="#fff" stroke="#111" stroke-width="2" stroke-linejoin="round"/></svg>
        </li>
        <li class="dropdown-item"><span class="item-arrow"><svg width="10" height="12" viewBox="0 0 10 12"><path d="M2 1 L8 6 L2 11" fill="none" stroke="#fff" stroke-width="2.5"/></svg></span>Disability</li>
        <li class="dropdown-item"><span class="item-arrow"><svg width="10" height="12" viewBox="0 0 10 12"><path d="M2 1 L8 6 L2 11" fill="none" stroke="#fff" stroke-width="2.5"/></svg></span>Office-overhead</li>
        <li class="dropdown-item"><span class="item-arrow"><svg width="10" height="12" viewBox="0 0 10 12"><path d="M2 1 L8 6 L2 11" fill="none" stroke="#fff" stroke-width="2.5"/></svg></span>Personal accident</li>
        <li class="dropdown-item"><span class="item-arrow"><svg width="10" height="12" viewBox="0 0 10 12"><path d="M2 1 L8 6 L2 11" fill="none" stroke="#fff" stroke-width="2.5"/></svg></span>Travel</li>
        <li class="dropdown-item"><span class="item-arrow"><svg width="10" height="12" viewBox="0 0 10 12"><path d="M2 1 L8 6 L2 11" fill="none" stroke="#fff" stroke-width="2.5"/></svg></span>Medical evacuation</li>
        <li class="dropdown-item"><span class="item-arrow"><svg width="10" height="12" viewBox="0 0 10 12"><path d="M2 1 L8 6 L2 11" fill="none" stroke="#fff" stroke-width="2.5"/></svg></span>Critical illness</li>
        <li class="dropdown-item"><span class="item-arrow"><svg width="10" height="12" viewBox="0 0 10 12"><path d="M2 1 L8 6 L2 11" fill="none" stroke="#fff" stroke-width="2.5"/></svg></span>Hospital indemnity</li>
      </ul>

      <div class="social-links">
        <span class="social-icon network-one" role="img" aria-label="Social network link"></span>
        <span class="social-icon network-two" role="img" aria-label="Video channel link"></span>
        <span class="social-icon network-three" role="img" aria-label="Social network link"></span>
        <span class="social-icon network-four" role="img" aria-label="Professional network link"></span>
      </div>

      <div class="brand">
        <div class="brand-row">
          <span class="brand-mark"></span>
          <p class="brand-name"><span>Lone Prairie Physicians</span><span>Insurance Trust</span></p>
        </div>
        <p class="brand-endorsement">Exclusively endorsed by the Lone Prairie Medical Society</p>
      </div>
    </div>
  </div>
</body>
</html>
```